Concrete Grinding and Polishing company business card with logo, based in Australia.

We need a business card design along with logo for a new company based in Melbourne called BrightLap. We specialise in the grinding and polishing of concrete. Polished concrete is durable, easy to maintain, cost effective, dust proof, has increased light reflectivity, and is slip resistant, among other benefits. In short, polished concrete is a popular flooring solution because of its practical advantages, as well as it's decorative appeal.

Industry/Entity Type

Business

Requirements
Must have
• It must have the company name(BrightLap) as well as the slogan: A Cut Above The Rest.
Nice to have
• Something that symbolises polished concrete. Would also like it to have a silver background with black writing, if possible.

```html
<!DOCTYPE html>
<html lang="en">
<head>
<meta charset="utf-8">
<title>BrightLap Business Card</title>
<link rel="stylesheet" href="https://fonts.googleapis.com/css2?family=Noto+Sans:ital,wght@0,400;0,500;1,400&display=swap">
<style>
  :root {
    --paper: #ffffff;
    --band: #6f6e6c;
    --brand-grey: #666565;
    --text-light: #ffffff;
    --frame: #2a2a2a;
  }
  html, body {
    margin: 0;
    padding: 0;
    width: 1200px;
    height: 688px;
    overflow: hidden;
    background: var(--paper);
  }
  .card {
    position: relative;
    width: 1200px;
    height: 688px;
    box-sizing: border-box;
    border: 1px solid var(--frame);
    background: var(--paper);
    font-family: "Noto Sans", sans-serif;
    overflow: hidden;
  }
  .brand-mark {
    position: absolute;
    left: 205px;
    top: 29px;
    width: 164px;
    height: 164px;
  }
  .brand-name {
    position: absolute;
    left: 390px;
    top: 14px;
    margin: 0;
    font-size: 98px;
    font-weight: 500;
    line-height: 1.2;
    letter-spacing: -1px;
    color: var(--brand-grey);
  }
  .brand-tagline {
    position: absolute;
    left: 392px;
    top: 146px;
    margin: 0;
    font-size: 31px;
    font-weight: 400;
    line-height: 1.2;
    letter-spacing: 0.5px;
    color: var(--brand-grey);
  }
  .contact-band {
    position: absolute;
    left: 0;
    top: 302px;
    width: 100%;
    height: 386px;
    background: var(--band);
    color: var(--text-light);
    text-align: center;
  }
  .person-name {
    position: absolute;
    left: 0;
    right: 0;
    top: 20px;
    margin: 0;
    font-size: 70px;
    font-style: italic;
    font-weight: 400;
    line-height: 1.2;
    letter-spacing: 1px;
  }
  .contact-details {
    position: absolute;
    left: 0;
    right: 0;
    top: 194px;
    margin: 0;
    font-style: normal;
    font-size: 29px;
    line-height: 39px;
  }
  .contact-details span { display: block; }
</style>
</head>
<body>
  <div class="card">
    <svg class="brand-mark" viewBox="0 0 164 164" aria-hidden="true">
      <circle cx="82" cy="82" r="82" fill="var(--brand-grey)"/>
    </svg>
    <h1 class="brand-name">BrightLap</h1>
    <p class="brand-tagline">A Cut Above The Rest</p>

    <section class="contact-band">
      <h2 class="person-name">Dana Whitfield</h2>
      <address class="contact-details">
        <span>Shipping: 27 Kiln Street, Brunswick, VIC 3056</span>
        <span>Mailing: P.O. Box 219, Brunswick, VIC 3056</span>
        <span>Tel: (03) 9555 0142, Fax: (03) 9555 0187</span>
        <span>Email:sales@brightlap.com.au</span>
      </address>
    </section>
  </div>
</body>
</html>
```